Stationary and Logo Design Project

We need a full corporate logo and stationary design for our company Lumvira7Q. Lumvira7Q specializes in creating custom adult sex toys using CAD and 3D Printing technologies as part of the process. The companies tagline is "Your Pleasure, Your Way", though this is not required to be part of the logo.

We are looking for something sensual, romantic and sexy, but not something explicit and vulgar.

As the company will be targeting mid to high-end clientele tastefulness is very important to us - this is difficult when the service we are selling is sex but can be achieved.

What we are after:

1. Logo
2. Business Card Design
3. Letterhead Design
4. Email Signature Design

File Formats we require in colour, greyscale and Black and White:

1 .AI
2 .EPS
3 .TIF
4 .PDF
5 .PNG (300 dpi)
6 .JPG (300 dpi)
7 .GIF (300 dpi)

Target Market(s)

Adults between the ages of 21 and 50 (Predominantly female but not limited to) who like there sex toys and want a custom job.

Industry/Entity Type

Adult

Requirements
Must have
• As we are planning on advertising in the future make sure the art is suitable for print advertising.
Nice to have
• The tagline "Your Pleasure, Your Way" on the business card, letterhead and email signature.
Should not have
• Explicit/vulgar illustrations.

"Clip-Art" should not be used.

```html
<!DOCTYPE html>
<html lang="en">
<head>
<meta charset="utf-8">
<title>Lumvira7Q Email Signature</title>
<link rel="stylesheet" href="https://fonts.googleapis.com/css2?family=Didact+Gothic&family=Caudex:ital@1&display=swap">
<style>
  :root {
    --canvas: #ffffff;
    --blush-strong: #ffc8fb;
    --blush-soft: #fde6fb;
    --ink-dark: #3a3a3a;
    --ink-label: #9a9a9a;
    --ink-small: #555555;
    --accent: #ff33cc;
  }
  html, body {
    margin: 0;
    padding: 0;
    width: 1200px;
    height: 384px;
    overflow: hidden;
    background: var(--canvas);
  }
  .signature {
    position: relative;
    width: 1200px;
    height: 384px;
    background: var(--canvas);
    font-family: "Didact Gothic", "Century Gothic", sans-serif;
    overflow: hidden;
  }
  .header-band {
    position: absolute;
    left: 0;
    top: 0;
    width: 1200px;
    height: 250px;
    border-radius: 46px 46px 0 0;
    background: linear-gradient(to bottom, var(--blush-strong) 0%, var(--blush-soft) 55%, var(--canvas) 100%);
  }
  .brand-name {
    position: absolute;
    left: 36px;
    top: -8px;
    margin: 0;
    font-family: "Didact Gothic", "Century Gothic", sans-serif;
    font-weight: 400;
    font-size: 128px;
    letter-spacing: -2px;
    line-height: 1;
    color: var(--ink-dark);
  }
  .tagline {
    position: absolute;
    left: 42px;
    top: 122px;
    margin: 0;
    font-family: "Caudex", Georgia, serif;
    font-style: italic;
    font-size: 19px;
    color: var(--ink-dark);
  }
  .contact-fields {
    position: absolute;
    left: 38px;
    top: 180px;
    margin: 0;
    padding: 0;
    list-style: none;
  }
  .contact-fields li {
    font-size: 31px;
    line-height: 40px;
    color: var(--ink-label);
  }
  .qualities {
    position: absolute;
    top: 364px;
    left: 0;
    width: 1200px;
    margin: 0;
    padding: 0;
    list-style: none;
    font-size: 14px;
    color: var(--ink-small);
  }
  .qualities li {
    position: absolute;
    top: 0;
    white-space: nowrap;
  }
  .qualities .initial { color: var(--accent); }
  .q-glamorous { left: 694px; }
  .q-gorgeous { left: 845px; }
  .q-gratifying { left: 1012px; }
  .q-genuine { left: 1130px; }
</style>
</head>
<body>
<div class="signature">
  <div class="header-band"></div>
  <h1 class="brand-name">Lumvira7Q</h1>
  <p class="tagline">Your Pleasure, Your Way</p>
  <ul class="contact-fields">
    <li>Name/Signature:</li>
    <li>Address:</li>
    <li>Email:</li>
    <li>Contact Number:</li>
    <li>Website:</li>
  </ul>
  <ul class="qualities">
    <li class="q-glamorous"><span class="initial">g</span>lamorous</li>
    <li class="q-gorgeous"><span class="initial">g</span>orgeous</li>
    <li class="q-gratifying"><span class="initial">g</span>ratifying</li>
    <li class="q-genuine"><span class="initial">g</span>enuine</li>
  </ul>
</div>
</body>
</html>
```